Business Card Design Project

Business card design for an IT Service company. A logo has already been created in a different contest and has been attached to this project. Ideally we're looking for a double sided business card that matches the look and feel of our newly created logo.

We're open to creativity if you feel a tag line is needed such as "IT Services and Application Development". We're open to really and look and feel - even single sided business cards if you feel you have something that's a great idea.

Last thought here - I'm not sure how it'll look but maybe a two tone card? One side dark blue and the other side white? Don't limit the design submissions to this tho - just curious if it would look good

Nothing too busy please - simple... Thank you and happy designing!

Target Market(s)

Businesses that require IT Services and support for hosted services, technical consultation, web design.

Industry/Entity Type

Business

Font styles to use
Sans Serif

Requirements
Must have
• Use the colors provided in the logo (see attachment) or additional colors that compliment
Must have the following contact info (not necessarily in this order):
- Alan Fisk
- Founding Partner
- afisk@quillbarrow.example
- 555-382-1946
- www.quillbarrow.example

```html
<!DOCTYPE html>
<html lang="en">
<head>
<meta charset="utf-8">
<title>Quillbarrow Business Card</title>
<link href="https://fonts.googleapis.com/css2?family=Open+Sans:wght@400;600;700&display=swap" rel="stylesheet">
<style>
  :root {
    --navy: #1f2d5c;
    --navy-deep: #19244b;
    --navy-back: #2c3c6e;
    --navy-faint: #25335f;
    --white: #ffffff;
    --ink: #1f2d5c;
    --ink-soft: #3a4670;
    --accent-blue: #4a86c5;
    --accent-green: #7a9a3a;
    --page: #e9ebef;
  }
  * { margin: 0; padding: 0; box-sizing: border-box; }
  html, body {
    width: 1200px; height: 800px; overflow: hidden;
    background: var(--page);
    font-family: "Open Sans", Arial, sans-serif;
  }
  .canvas {
    width: 1200px; height: 800px;
    display: flex; align-items: center; justify-content: center; gap: 40px;
  }
  .card {
    width: 540px; height: 310px; position: relative; overflow: hidden;
    box-shadow: 0 6px 18px rgba(20, 30, 60, 0.18);
  }

  /* Front */
  .card-front { background: var(--white); }
  .brand {
    position: absolute; left: 36px; top: 82px;
    display: flex; align-items: center; gap: 12px;
  }
  .brand-dot {
    width: 22px; height: 22px; border-radius: 50%;
    background: var(--accent-blue);
  }
  .brand-name {
    font-size: 30px; font-weight: 700; color: var(--ink); letter-spacing: -0.3px;
  }
  .divider {
    position: absolute; left: 300px; top: 52px;
    width: 1px; height: 118px; background: var(--ink-soft);
  }
  .person {
    position: absolute; left: 322px; top: 86px; color: var(--ink);
  }
  .person-name { font-size: 26px; font-weight: 700; line-height: 1.1; }
  .person-role { font-size: 14px; font-weight: 400; color: var(--ink-soft); margin-top: 2px; }

  .contact-band {
    position: absolute; left: 0; right: 0; bottom: 0; height: 90px;
    background: linear-gradient(180deg, var(--navy) 0%, var(--navy-deep) 100%);
    display: grid; grid-template-columns: 1fr 1.3fr 1fr; align-items: center;
  }
  .contact-item {
    display: flex; flex-direction: column; align-items: center; gap: 8px;
    color: var(--white); font-size: 12.5px;
  }
  .contact-icon {
    width: 28px; height: 28px; border-radius: 50%;
    background: var(--white); display: flex; align-items: center; justify-content: center;
  }
  .contact-icon svg { width: 16px; height: 16px; }

  /* Back */
  .card-back {
    background: linear-gradient(160deg, var(--navy-back) 0%, var(--navy) 100%);
    display: flex; align-items: center; justify-content: center;
  }
  .back-name {
    font-size: 64px; font-weight: 700; color: var(--navy-faint); letter-spacing: -0.5px;
  }
</style>
</head>
<body>
<main class="canvas">
  <section class="card card-front" aria-label="Business card front">
    <div class="brand">
      <span class="brand-dot"></span>
      <span class="brand-name">Quillbarrow</span>
    </div>
    <div class="divider"></div>
    <div class="person">
      <div class="person-name">Alan Fisk</div>
      <div class="person-role">Founding Partner</div>
    </div>
    <div class="contact-band">
      <div class="contact-item">
        <span class="contact-icon">
          <svg viewBox="0 0 16 16" aria-hidden="true"><rect x="4.5" y="1.5" width="7" height="13" rx="1.3" fill="none" stroke="#1f2d5c" stroke-width="1.5"/><rect x="6" y="3.5" width="4" height="6" fill="#1f2d5c"/><circle cx="8" cy="12.2" r="0.9" fill="#1f2d5c"/></svg>
        </span>
        <span class="contact-text">555-382-1946</span>
      </div>
      <div class="contact-item">
        <span class="contact-icon">
          <svg viewBox="0 0 16 16" aria-hidden="true"><rect x="1.5" y="3.5" width="13" height="9" fill="none" stroke="#1f2d5c" stroke-width="1.5"/><path d="M1.5 3.5 L8 9 L14.5 3.5" fill="none" stroke="#1f2d5c" stroke-width="1.5"/></svg>
        </span>
        <span class="contact-text">afisk@quillbarrow.example</span>
      </div>
      <div class="contact-item">
        <span class="contact-icon">
          <svg viewBox="0 0 16 16" aria-hidden="true"><circle cx="8" cy="8" r="6.3" fill="none" stroke="#1f2d5c" stroke-width="1.4"/><ellipse cx="8" cy="8" rx="2.8" ry="6.3" fill="none" stroke="#1f2d5c" stroke-width="1.2"/><line x1="1.7" y1="8" x2="14.3" y2="8" stroke="#1f2d5c" stroke-width="1.2"/></svg>
        </span>
        <span class="contact-text">www.quillbarrow.example</span>
      </div>
    </div>
  </section>

  <section class="card card-back" aria-label="Business card back">
    <span class="back-name">Quillbarrow</span>
  </section>
</main>
</body>
</html>
```